Tech business card design

We need an amazing business card design for our new business 'Brakka' a marketing tech startup based in Sydney, Australia. We provide an online marketplace for businesses to search and buy advertising media, connect with service providers and learn more about marketing. We wish to communicate 'cool tech', reliability and professionalism and design based around our logo.

Target Market(s)

Business Owners

Contact Information for Business Card

Name
Position
Email Address
Website
Phone Number

Font styles to use
Other font styles liked:
• Avenir & Avenir Next

Colors

Designer to choose colors to be used in the design.

```html
<!DOCTYPE html>
<html lang="en">
<head>
<meta charset="utf-8">
<title>Brakka Business Card</title>
<link rel="stylesheet" href="https://fonts.googleapis.com/css2?family=Nunito+Sans:wght@400;700;800;900&display=swap">
<style>
  :root {
    --navy: #14194a;
    --navy-soft: #1b2156;
    --grey: #7a7a7c;
    --white: #ffffff;
    --back-mark: #4f5684;
    --stage: #2a2a2c;
  }
  * { margin: 0; padding: 0; box-sizing: border-box; }
  html, body {
    width: 1200px; height: 803px; overflow: hidden;
    background: var(--stage);
    font-family: "Nunito Sans", Arial, sans-serif;
  }
  .card {
    position: absolute;
    width: 520px; height: 297px;
    overflow: hidden;
    box-shadow: 0 12px 30px rgba(0,0,0,0.45);
  }
  .card--front { left: 60px; top: 253px; background: var(--white); }
  .card--back  { left: 620px; top: 253px; background: var(--navy-soft); }
  .card__shapes { position: absolute; inset: 0; }
  .brand-name {
    position: absolute; left: 28px; top: 30px;
    font-size: 78px; font-weight: 900; color: var(--navy);
    letter-spacing: -1px; line-height: 1;
  }
  .brand-tm {
    position: absolute; left: 302px; top: 42px;
    font-size: 10px; font-weight: 700; color: var(--navy);
  }
  .person { position: absolute; left: 34px; top: 220px; color: var(--white); }
  .person__name { font-size: 15px; font-weight: 800; letter-spacing: 0.3px; }
  .person__role { font-size: 11px; font-weight: 700; margin-left: 10px; }
  .contact-list { list-style: none; margin-top: 8px; margin-left: 14px; }
  .contact-list li {
    display: flex; align-items: center; gap: 7px;
    font-size: 12px; line-height: 18px;
  }
  .contact-list svg { width: 11px; height: 11px; fill: var(--white); }
  .address {
    position: absolute; right: 22px; top: 130px;
    text-align: right; color: var(--white);
    font-size: 12px; line-height: 16px;
  }
  .address__web { margin-top: 8px; }
  .back-mark {
    position: absolute; left: 70px; top: 90px;
    font-size: 120px; font-weight: 900; color: var(--back-mark);
    letter-spacing: -2px; line-height: 1;
  }
  .back-tm {
    position: absolute; left: 452px; top: 108px;
    font-size: 11px; font-weight: 700; color: var(--back-mark);
  }
</style>
</head>
<body>
  <section class="card card--front" aria-label="Business card front">
    <svg class="card__shapes" viewBox="0 0 520 297" aria-hidden="true">
      <polygon fill="var(--navy)" points="0,200 205,200 285,135 235,128 340,115 520,115 520,297 0,297"/>
      <polygon fill="var(--white)" points="215,297 300,190 395,297"/>
      <polygon fill="var(--grey)" points="242,297 300,218 365,297"/>
      <rect fill="var(--white)" x="0" y="284" width="520" height="13"/>
    </svg>
    <div class="brand-name">Brakka</div>
    <div class="brand-tm">TM</div>
    <div class="person">
      <div class="person__name">JOHN SMITH</div>
      <div class="person__role">Position</div>
      <ul class="contact-list">
        <li>
          <svg viewBox="0 0 24 24" aria-hidden="true"><path d="M6.6 10.8a15.1 15.1 0 0 0 6.6 6.6l2.2-2.2c.3-.3.7-.4 1-.2 1.1.4 2.3.6 3.6.6.6 0 1 .4 1 1V20c0 .6-.4 1-1 1A17 17 0 0 1 3 4c0-.6.4-1 1-1h3.5c.6 0 1 .4 1 1 0 1.3.2 2.5.6 3.6.1.3 0 .7-.2 1z"/></svg>
          012-345-6789
        </li>
        <li>
          <svg viewBox="0 0 24 24" aria-hidden="true"><path d="M2 5h20v14H2zm2 2v.4l8 5 8-5V7zm0 2.8V17h16V9.8l-8 5z"/></svg>
          info@brakka.com
        </li>
      </ul>
    </div>
    <div class="address">
      <div>Street Name, City Name</div>
      <div>Zipcode:012345</div>
      <div class="address__web">www.brakka.com</div>
    </div>
  </section>

  <section class="card card--back" aria-label="Business card back">
    <div class="back-mark">Brakka</div>
    <div class="back-tm">TM</div>
  </section>
</body>
</html>
```